International Hand & Body company needing a Hand cream tube design for the Retail market

I am wanting a modern design for a new range of 6 hand creams I will be launching in August. They need to compliment our range of wrapped soaps which you can see on www.plomvane.com.au so am wanting clean designs. I am wanting a solid colour with a hand drawn organic feel line drawing in black elegantly placed wrapping around the label. I am wanting to focus on the colour and positioning of words and fonts. I like modern clean contemporary fonts. The final design needs to appeal to the broader female market.This may lead to range expansion if designs are well received.
Updates

These designs are not hitting the brief. They are too generic and look like a supermarket brand. Our brand is more boutique and this design needs to be modern and simple. I would like more solid colours and more modern designs. Without patterns.

Target Market(s)

Female aged 20 - 70

Requirements
Must have
• a modern contemporary design that will appeal to the masses.
• Please read attached brief.
Should not have
• a black botanical illustration, in a loose and organic design to match the fragrance.

```html
<!DOCTYPE html>
<html lang="en">
<head>
<meta charset="utf-8">
<title>Hand Cream Range – Label Fronts</title>
<link href="https://fonts.googleapis.com/css2?family=Josefin+Sans:wght@300;400&display=swap" rel="stylesheet">
<style>
  :root {
    --backdrop: #0a3d6e;
    --rose-base: #f8d3df;
    --rose-brush: #e2657d;
    --rose-ink: #e0455f;
    --blossom-base: #fde3c6;
    --blossom-brush: #eda27f;
    --blossom-ink: #c9653d;
  }
  * { box-sizing: border-box; margin: 0; padding: 0; }
  html, body {
    width: 1200px; height: 1200px; overflow: hidden;
    background: var(--backdrop);
  }
  .range {
    position: relative; width: 1200px; height: 1200px;
    font-family: "Josefin Sans", "Helvetica Neue", Arial, sans-serif;
  }
  .label {
    position: absolute; top: 110px; width: 440px; height: 840px;
    overflow: hidden;
  }
  .label--rose { left: 70px; background: var(--rose-base); color: var(--rose-ink); }
  .label--blossom { left: 605px; background: var(--blossom-base); color: var(--blossom-ink); }
  .label__brush {
    position: absolute; left: 20px; top: 70px; width: 400px; height: 560px;
  }
  .label__logo {
    position: absolute; top: 148px; left: 0; right: 0; text-align: center;
    font-weight: 300; font-size: 24px; letter-spacing: 0.2em;
  }
  .label__scent {
    position: absolute; top: 726px; left: 0; right: 0; text-align: center;
    font-weight: 300; font-size: 22px; line-height: 27px; letter-spacing: 0.16em;
    text-transform: uppercase;
  }
  .label__volume {
    position: absolute; top: 796px; left: 0; right: 0; text-align: center;
    font-weight: 300; font-size: 13px; letter-spacing: 0.18em;
  }
</style>
</head>
<body>
<main class="range">
  <section class="label label--rose">
    <svg class="label__brush" viewBox="0 0 400 560" role="img" aria-label="Loose hand-painted brush circle in rose pink">
      <defs>
        <radialGradient id="roseWash" cx="50%" cy="50%" r="50%">
          <stop offset="0%" stop-color="#e2657d" stop-opacity="0.85"/>
          <stop offset="78%" stop-color="#e2657d" stop-opacity="0.7"/>
          <stop offset="100%" stop-color="#e2657d" stop-opacity="0"/>
        </radialGradient>
      </defs>
      <ellipse cx="200" cy="280" rx="195" ry="270" fill="url(#roseWash)"/>
    </svg>
    <div class="label__logo">LOGO</div>
    <div class="label__scent">Wild Rose<br>&amp;Neroli</div>
    <div class="label__volume">125 ML</div>
  </section>

  <section class="label label--blossom">
    <svg class="label__brush" viewBox="0 0 400 560" role="img" aria-label="Loose hand-painted brush circle in soft peach">
      <defs>
        <radialGradient id="blossomWash" cx="50%" cy="50%" r="50%">
          <stop offset="0%" stop-color="#eda27f" stop-opacity="0.85"/>
          <stop offset="78%" stop-color="#eda27f" stop-opacity="0.7"/>
          <stop offset="100%" stop-color="#eda27f" stop-opacity="0"/>
        </radialGradient>
      </defs>
      <ellipse cx="200" cy="280" rx="195" ry="270" fill="url(#blossomWash)"/>
    </svg>
    <div class="label__logo">LOGO</div>
    <div class="label__scent">Orange Blossom<br>&amp;Lime</div>
    <div class="label__volume">125 ML</div>
  </section>
</main>
</body>
</html>
```